RLTP Business Card Design

I have a rough idea of the design / layout of the company business card but need help in finalizing the design and quality.

I'm looking for the card to be stand out, but simple, on the front with clear detail on the back with space for some one to write any other detail they need onto the card. The rough draft includes the crinkled graph paper back ground which I quite like for the front.

I will need the card design completed and ready to print in Australian business card standard sizes. This includes detail on all colors, fonts and type faces used as well as copy of the original for editing (inserting other employee details).

I have included the company logo and a rough draft of the card, including the graphic I would like to use for the back ground on the front, I am not sure that the graphic is any good for printing, not the highest res.

Thanks,

Owen

```html
<!DOCTYPE html>
<html lang="en">
<head>
<meta charset="utf-8">
<title>RLTP Business Card</title>
<link rel="stylesheet" href="https://fonts.googleapis.com/css2?family=Montserrat:wght@300;400;700;800&display=swap">
<style>
  :root {
    --page-bg: #e9e9e7;
    --card-white: #f7f7f9;
    --card-grey: #dcdcdc;
    --ink: #1e1e1e;
    --ink-soft: #3a3a3a;
    --rule: #5a5a5a;
    --icon-bg: #4a4a4a;
    --icon-fg: #f2f2f2;
    --paper-top: #f4f4f8;
    --paper-bottom: #e4e5ee;
  }
  * { box-sizing: border-box; margin: 0; padding: 0; }
  html, body { width: 1200px; height: 900px; overflow: hidden; }
  body {
    background: var(--page-bg);
    font-family: "Montserrat", sans-serif;
    color: var(--ink);
    display: flex;
    align-items: center;
    justify-content: center;
    gap: 40px;
  }
  .card {
    position: relative;
    width: 520px;
    height: 318px;
    border-radius: 3px;
    box-shadow: 0 6px 18px rgba(0,0,0,.15);
    overflow: hidden;
  }
  /* Front */
  .card-front { background: var(--card-white); }
  .paper-texture {
    position: absolute; inset: 0;
    background: linear-gradient(160deg, var(--paper-top), var(--paper-bottom));
  }
  .brand {
    position: absolute;
    right: 44px;
    top: 118px;
    text-align: left;
  }
  .brand-name {
    font-weight: 800;
    font-size: 78px;
    letter-spacing: 2px;
    line-height: .9;
    color: var(--ink);
  }
  .brand-tagline {
    font-weight: 800;
    font-size: 12.5px;
    letter-spacing: .4px;
    text-transform: uppercase;
    color: var(--ink);
    margin-top: 4px;
  }
  /* Back */
  .card-back { background: var(--card-grey); padding: 44px 40px; }
  .person {
    display: flex;
    align-items: baseline;
    gap: 12px;
    padding-bottom: 10px;
    border-bottom: 1px solid var(--rule);
    width: 330px;
  }
  .person-name {
    font-weight: 400;
    font-size: 20px;
    letter-spacing: 1px;
    text-transform: uppercase;
    color: var(--ink);
  }
  .person-role {
    font-weight: 400;
    font-size: 13px;
    color: var(--ink-soft);
  }
  .contact-list { list-style: none; margin-top: 22px; }
  .contact-item {
    display: flex;
    align-items: flex-start;
    gap: 12px;
    font-size: 14px;
    font-weight: 400;
    color: var(--ink-soft);
    line-height: 1.15;
    margin-bottom: 9px;
  }
  .contact-icon {
    flex: none;
    width: 20px; height: 20px;
    border-radius: 50%;
    background: var(--icon-bg);
    display: flex; align-items: center; justify-content: center;
  }
  .contact-icon svg { width: 12px; height: 12px; fill: none; stroke: var(--icon-fg); stroke-width: 1.6; stroke-linecap: round; stroke-linejoin: round; }
</style>
</head>
<body>

<section class="card card-front" aria-label="Card front">
  <div class="paper-texture" role="img" aria-label="Crinkled lined paper background texture"></div>
  <div class="brand">
    <div class="brand-name">RLTP</div>
    <div class="brand-tagline">Reliable Live Tech Productions</div>
  </div>
</section>

<section class="card card-back" aria-label="Card back">
  <div class="person">
    <span class="person-name">Owen Hale</span>
    <span class="person-role">Operations Manager</span>
  </div>
  <ul class="contact-list">
    <li class="contact-item">
      <span class="contact-icon"><svg viewBox="0 0 12 12"><rect x="3" y="1" width="6" height="10" rx="1"/><line x1="5.5" y1="9" x2="6.5" y2="9"/></svg></span>
      0400 128 764
    </li>
    <li class="contact-item">
      <span class="contact-icon"><svg viewBox="0 0 12 12"><path d="M2.5 2h2l1 2.5-1.3 1a6 6 0 0 0 2.3 2.3l1-1.3 2.5 1v2a1 1 0 0 1-1 1A8.5 8.5 0 0 1 1.5 3a1 1 0 0 1 1-1z"/></svg></span>
      9000 3812
    </li>
    <li class="contact-item">
      <span class="contact-icon"><svg viewBox="0 0 12 12"><rect x="1.5" y="3" width="9" height="6.5" rx=".5"/><path d="M1.5 3.3 6 7l4.5-3.7"/></svg></span>
      ohale@rltp.com.au
    </li>
    <li class="contact-item">
      <span class="contact-icon"><svg viewBox="0 0 12 12"><rect x="3" y="1.5" width="6" height="9" rx="3"/><line x1="6" y1="3" x2="6" y2="5"/></svg></span>
      www.rltp.com.au
    </li>
    <li class="contact-item">
      <span class="contact-icon"><svg viewBox="0 0 12 12"><path d="M6 11S2.5 7.2 2.5 4.8a3.5 3.5 0 0 1 7 0C9.5 7.2 6 11 6 11z"/><circle cx="6" cy="4.8" r="1.2"/></svg></span>
      <span>4/52 Harbour Lane Melbourne 3000<br>Melbourne / Perth</span>
    </li>
  </ul>
</section>

</body>
</html>
```